One Pager Fact Sheet Design

I need a couple of headers and footer designed to use for information security fact sheets to give to customers. Similar to the one listed below.

```html
<!DOCTYPE html>
<html lang="en">
<head>
<meta charset="utf-8">
<title>Corelink Data – Fact Sheet Headers &amp; Footers</title>
<link rel="stylesheet" href="https://fonts.googleapis.com/css2?family=Orbitron:wght@500;700&family=Roboto+Condensed:wght@300;400;700&display=swap">
<style>
  :root {
    --red: #e0141e;
    --red-dark: #c10f18;
    --grey: #58595b;
    --ink: #222;
    --text: #3a3a3a;
    --soft: #e6e6e6;
    --white: #fff;
    --display: "Orbitron", sans-serif;
    --body: "Roboto Condensed", sans-serif;
  }
  * { box-sizing: border-box; margin: 0; padding: 0; }
  html, body { width: 1162px; height: 1200px; overflow: hidden; background: var(--white); }
  body { position: relative; font-family: var(--body); color: var(--text); }

  /* ===== Shared header pieces ===== */
  .header { position: absolute; overflow: visible; }
  .tagline-band {
    position: absolute; left: 0; top: 0; width: 100%;
    background: var(--grey); color: var(--white);
    font-family: var(--display); font-weight: 500; text-align: center; white-space: nowrap;
  }
  .red-panel {
    position: absolute; left: 0;
    background: linear-gradient(180deg, var(--red) 0%, var(--red-dark) 100%);
    color: var(--white);
  }
  .map-area {
    position: absolute; inset: 0;
    background: radial-gradient(ellipse at 45% 40%, rgba(120,0,0,.28) 0%, rgba(120,0,0,0) 65%);
  }
  .services { position: absolute; list-style: none; font-weight: 300; white-space: nowrap; }
  .services li::before { content: "• "; }
  .phone-line { position: absolute; display: flex; align-items: center; font-weight: 700; }
  .date { position: absolute; font-weight: 700; white-space: nowrap; }
  .brand-panel {
    position: absolute; top: 0; background: var(--white);
    text-align: center; box-shadow: 0 6px 6px -4px rgba(0,0,0,.15);
  }
  .brand {
    display: inline-flex; align-items: center; color: var(--red);
    font-family: var(--body); font-weight: 700; white-space: nowrap;
  }
  .brand-dot { border-radius: 50%; border: solid var(--red); flex: none; }
  .fact-title { font-family: var(--display); font-weight: 700; color: var(--red); letter-spacing: .02em; }
  .fact-sub { color: #555; font-weight: 300; }

  /* ===== Large banner ===== */
  .banner { left: 100px; top: 99px; width: 958px; height: 220px; }
  .banner .tagline-band { height: 53px; line-height: 57px; font-size: 19px; letter-spacing: .185em; }
  .banner .red-panel { top: 53px; width: 640px; height: 167px; }
  .banner .services { top: 17px; font-size: 15px; line-height: 17px; }
  .banner .services.col-a { left: 134px; }
  .banner .services.col-b { left: 394px; }
  .banner .phone-line { left: 137px; top: 104px; font-size: 19px; gap: 17px; }
  .banner .date { right: 36px; top: 113px; font-size: 22px; }
  .banner .brand-panel { left: 628px; top: 52px; width: 330px; height: 168px; border-top-left-radius: 12px; padding-top: 26px; }
  .banner .brand { font-size: 28px; gap: 8px; }
  .banner .brand-dot { width: 30px; height: 30px; border-width: 5px; }
  .banner .fact-title { font-size: 27px; margin-top: 18px; }
  .banner .fact-sub { font-size: 15px; line-height: 21px; margin-top: 0; }

  /* ===== Pages ===== */
  .page {
    position: absolute; top: 471px; width: 433px; height: 612px; background: var(--white);
    box-shadow: 0 14px 30px rgba(0,0,0,.18), 0 0 4px rgba(0,0,0,.06);
  }
  .page-left { left: 99px; }
  .page-right { left: 627px; }
  .page .tagline-band { height: 25px; line-height: 26px; font-size: 9px; letter-spacing: .17em; }

  .page-left .red-panel { top: 25px; width: 284px; height: 75px; }
  .page-left .services { top: 10px; font-size: 5.4px; line-height: 7.6px; }
  .page-left .services.col-a { left: 60px; }
  .page-left .services.col-b { left: 177px; }
  .page-left .phone-line { left: 62px; top: 50px; font-size: 7.5px; gap: 8px; }
  .page-left .date { right: 14px; top: 52px; font-size: 9px; }
  .page-left .brand-panel { left: 284px; top: 25px; width: 149px; height: 75px; border-top-left-radius: 5px; padding-top: 10px; }
  .page-left .brand { font-size: 12.5px; gap: 3px; }
  .page-left .brand-dot { width: 13px; height: 13px; border-width: 2.5px; }
  .page-left .fact-title { font-size: 12.5px; margin-top: 8px; }
  .page-left .fact-sub { font-size: 5.6px; line-height: 9px; }

  .slim-header { position: absolute; left: 0; top: 25px; width: 100%; height: 42px; box-shadow: 0 6px 6px -5px rgba(0,0,0,.18); }
  .slim-header .date { left: 216px; top: 14px; font-size: 8.5px; color: var(--ink); }
  .slim-header .brand { position: absolute; left: 303px; top: 11px; font-size: 12.5px; gap: 3px; }
  .slim-header .brand-dot { width: 13px; height: 13px; border-width: 2.5px; }

  .article-title { position: absolute; font-family: var(--display); font-weight: 500; font-size: 9.6px; color: var(--ink); white-space: nowrap; }
  .copy { position: absolute; width: 310px; font-size: 8px; line-height: 10.2px; color: var(--text); font-weight: 400; }
  .copy p + p { margin-top: 10px; }

  .pull-mark { position: absolute; font-family: Georgia, serif; font-weight: 700; font-size: 34px; line-height: 1; color: #d8d8d8; }
  .pull-rule { position: absolute; height: 1px; background: #e4e4e4; }

  .crime-table { position: absolute; left: 84px; top: 413px; width: 307px; border-collapse: collapse; font-size: 5.6px; color: var(--ink); }
  .crime-table th { font-weight: 700; text-align: left; padding: 2px 2px 3px; }
  .crime-table td { padding: 1.6px 2px; height: 11.6px; }
  .crime-table .num { text-align: right; }
  .crime-table .pct { text-align: center; width: 50px; }
  .crime-table .group td { background: var(--soft); font-weight: 700; }
  .crime-table .shade td { background: #efefef; }
  .crime-table tbody tr:last-child td { border-bottom: 1px solid #9fb6c6; }

  .photo {
    position: absolute; left: 84px; top: 369px; width: 306px; height: 160px;
    background: radial-gradient(ellipse at 58% 60%, #7fc3f0 0%, #2a6aa6 25%, #123456 55%, #0a1a2e 100%);
  }

  .page-footer { position: absolute; left: 0; top: 556px; width: 100%; height: 56px; }
  .footer-rule { position: absolute; left: 50px; right: 26px; top: 8px; height: 2px; background: linear-gradient(90deg, rgba(0,0,0,0), #cfcfcf 20%, #cfcfcf 80%, rgba(0,0,0,0)); }
  .footer-dot { position: absolute; left: 210px; top: 0; width: 16px; height: 16px; border-radius: 50%; border: 3px solid var(--red); background: var(--white); }
  .contacts { position: absolute; left: 0; right: 0; top: 27px; display: flex; justify-content: center; gap: 11px; font-size: 5.6px; color: var(--ink); font-weight: 700; }
  .contacts span { display: inline-flex; align-items: center; gap: 4px; }
  .contacts svg { flex: none; }
</style>
</head>
<body>

<!-- ===== Large header banner ===== -->
<header class="header banner">
  <div class="tagline-band">We Make Your Technology Problems Go Away For Good</div>
  <div class="red-panel">
    <div class="map-area" role="img" aria-label="Dotted world map pattern"></div>
    <ul class="services col-a">
      <li>Business Continuity Program</li>
      <li>24/7 Service Desk</li>
      <li>Technology Strategy And Consulting</li>
      <li>Security Awareness Training</li>
    </ul>
    <ul class="services col-b">
      <li>Vulnerability &amp; Threat Assessment</li>
      <li>Remote Management And Monitoring</li>
      <li>Private Cloud &amp; Cloud Integrations</li>
      <li>Email Migration Service</li>
    </ul>
    <div class="phone-line">
      <svg width="42" height="42" viewBox="0 0 42 42" aria-hidden="true">
        <path d="M34 10 A17 17 0 1 0 37 27" fill="none" stroke="#fff" stroke-width="2.4"/>
        <path d="M31 6 l4 4 -5 2z" fill="#fff"/>
        <path d="M9 27c2 4 5 6 8 7l2-3-3-2-2 1c-1-1-2-2-3-4l1-2-2-3z" fill="#fff"/>
        <text x="22" y="25" font-family="Roboto Condensed, sans-serif" font-weight="700" font-size="12" fill="#fff" text-anchor="middle">24/7</text>
      </svg>
      555-014-2290
    </div>
    <div class="date">April 26th, 2016</div>
  </div>
  <div class="brand-panel">
    <div class="brand"><span class="brand-dot"></span>corelink data</div>
    <div class="fact-title">FACT SHEET</div>
    <div class="fact-sub">Weekly Technology Security News<br>From Around The Web</div>
  </div>
</header>

<!-- ===== Page with full header ===== -->
<article class="page page-left">
  <div class="tagline-band">We Make Your Technology Problems Go Away For Good</div>
  <div class="red-panel">
    <div class="map-area" role="img" aria-label="Dotted world map pattern"></div>
    <ul class="services col-a">
      <li>Business Continuity Program</li>
      <li>24/7 Service Desk</li>
      <li>Technology Strategy And Consulting</li>
      <li>Security Awareness Training</li>
    </ul>
    <ul class="services col-b">
      <li>Vulnerability &amp; Threat Assessment</li>
      <li>Remote Management And Monitoring</li>
      <li>Private Cloud &amp; Cloud Integrations</li>
      <li>Email Migration Service</li>
    </ul>
    <div class="phone-line">
      <svg width="18" height="18" viewBox="0 0 42 42" aria-hidden="true">
        <path d="M34 10 A17 17 0 1 0 37 27" fill="none" stroke="#fff" stroke-width="3"/>
        <text x="22" y="26" font-family="Roboto Condensed, sans-serif" font-weight="700" font-size="13" fill="#fff" text-anchor="middle">24/7</text>
      </svg>
      555-014-2290
    </div>
    <div class="date">April 26th, 2016</div>
  </div>
  <div class="brand-panel">
    <div class="brand"><span class="brand-dot"></span>corelink data</div>
    <div class="fact-title">FACT SHEET</div>
    <div class="fact-sub">Weekly Technology Security News<br>From Around The Web</div>
  </div>

  <h2 class="article-title" style="left:62px; top:138px;">Multipurpose malware: Sometimes Trojans come in threes</h2>
  <div class="copy" style="left:84px; top:167px;">
    <p>Just in case a plain old Ransomware wasn't bad enough, malware authors have added a DDOS component to Tricorn. This malware attacks you in multiple different ways.</p>
  </div>
  <div class="pull-mark" style="left:83px; top:201px;">&ldquo;</div>
  <div class="pull-rule" style="left:108px; top:212px; width:125px;"></div>
  <div class="copy" style="left:84px; top:222px;">
    <p>As if ransomware weren't bad enough, now it's metastasizing: not just spreading rapidly but even picking up secondary characteristics. Take Tricorn, ransomware first spotted in the wild back in February 2016.</p>
    <p>Briefly, here is the sequence of events. First, Tricorn arrives in the form of an e-mail attachment. Once executed, the virus behaves like any other ransomware, encrypting files and demanding money for their safe return. But then, security researchers are finding, it confirms the computer's Internet connection and begins using the infected PC for other purposes, such as for a distributed denial-of-service (DDoS) attack or as a spambot.</p>
  </div>
  <div class="pull-rule" style="left:260px; top:321px; width:105px;"></div>
  <div class="pull-mark" style="left:368px; top:310px;">&rdquo;</div>

  <h2 class="article-title" style="left:62px; top:342px;">NCB Internet Crime Report</h2>
  <div class="copy" style="left:84px; top:371px;">
    <p>You don't have to be in the NCB to know that Ransomware and Business Email Compromise are two of the leading issues facing cybersecurity. All leading information security experts agree on that. But still – it's nice to have the NCB confirm it.</p>
  </div>
  <table class="crime-table">
    <thead>
      <tr><th>Category</th><th class="num" style="width:70px;">Summ($)</th><th class="pct">%</th></tr>
    </thead>
    <tbody>
      <tr class="group"><td colspan="3">Sources</td></tr>
      <tr><td>Category</td><td class="num">450,000</td><td class="pct">100</td></tr>
      <tr class="group"><td colspan="3">Uses</td></tr>
      <tr><td>Transaction</td><td class="num">37,500</td><td class="pct">X</td></tr>
      <tr class="shade"><td>Ransomware</td><td class="num">7,333</td><td class="pct">X</td></tr>
      <tr><td>Business Email</td><td class="num">20,000</td><td class="pct">X</td></tr>
    </tbody>
  </table>
  <div class="copy" style="left:84px; top:504px;">
    <p>You don't have to be in the NCB to know that Ransomware and Business Email Compromise are two of the leading issues facing cybersecurity. All leading information security experts agree on that. But still – it's nice to have the NCB confirm it.</p>
  </div>

  <footer class="page-footer">
    <div class="footer-rule"></div>
    <div class="footer-dot"></div>
    <div class="contacts">
      <span><svg width="8" height="6" viewBox="0 0 8 6"><rect width="8" height="6" fill="#e0141e"/><path d="M0 0l4 3 4-3" stroke="#fff" stroke-width=".8" fill="none"/></svg>hello@corelinkdata.com</span>
      <span><svg width="7" height="7" viewBox="0 0 7 7"><circle cx="3.5" cy="3.5" r="3.5" fill="#e0141e"/></svg>www.corelinkdata.com/</span>
      <span><svg width="7" height="7" viewBox="0 0 7 7"><rect width="7" height="7" rx="1.2" fill="#3a8fd6"/></svg>/corelinkdata</span>
    </div>
  </footer>
</article>

<!-- ===== Page with slim header ===== -->
<article class="page page-right">
  <div class="tagline-band">We Make Your Technology Problems Go Away For Good</div>
  <div class="slim-header">
    <div class="date">April 26th, 2016</div>
    <div class="brand"><span class="brand-dot"></span>corelink data</div>
  </div>

  <h2 class="article-title" style="left:0; width:100%; text-align:center; top:98px;">Multipurpose malware: Sometimes Trojans come in threes</h2>
  <div class="copy" style="left:84px; top:127px;">
    <p>Just in case a plain old Ransomware wasn't bad enough, malware authors have added a DDOS component to Tricorn. This malware attacks you in multiple different ways.</p>
    <p>As if ransomware weren't bad enough, now it's metastasizing: not just spreading rapidly but even picking up secondary characteristics. Take Tricorn, ransomware first spotted in the wild back in February 2016.</p>
    <p>Briefly, here is the sequence of events. First, Tricorn arrives in the form of an e-mail attachment. Once executed, the virus behaves like any other ransomware, encrypting files and demanding money for their safe return. But then, security researchers are finding, it confirms the computer's Internet connection and begins using the infected PC for other purposes, such as for a distributed denial-of-service (DDoS) attack or as a spambot.</p>
    <p>As if ransomware weren't bad enough, now it's metastasizing: not just spreading rapidly but even picking up secondary characteristics. Take Tricorn, ransomware first spotted in the wild back in February 2016.</p>
    <p>Briefly, here is the sequence of events. First, Tricorn arrives in the form of an e-mail attachment. Once executed, the virus behaves like any other ransomware, encrypting files and demanding money for their safe return. But then, security researchers are finding, it confirms the computer's Internet connection and begins using the infected PC for other purposes, such as for a distributed denial-of-service (DDoS) attack or as a spambot.</p>
  </div>
  <div class="photo" role="img" aria-label="Photo of a hand holding glowing floating device screens and app icons on a dark blue background"></div>

  <footer class="page-footer">
    <div class="footer-rule"></div>
    <div class="footer-dot"></div>
    <div class="contacts">
      <span><svg width="8" height="6" viewBox="0 0 8 6"><rect width="8" height="6" fill="#e0141e"/><path d="M0 0l4 3 4-3" stroke="#fff" stroke-width=".8" fill="none"/></svg>hello@corelinkdata.com</span>
      <span><svg width="7" height="7" viewBox="0 0 7 7"><circle cx="3.5" cy="3.5" r="3.5" fill="#e0141e"/></svg>www.corelinkdata.com/</span>
      <span><svg width="7" height="7" viewBox="0 0 7 7"><rect width="7" height="7" rx="1.2" fill="#3a8fd6"/></svg>/corelinkdata</span>
    </div>
  </footer>
</article>

</body>
</html>
```